Quill|Marlow & Petrie business card contest

We need a logo for an upscale boutique diversified company involved in real estate, investments, cattle, and more. Our businesses DO NOT need to be reflected in the business card nor do we want them noted. This is our logo and colors and we love our logo and colors. Our logo looks best against a black background and we like to include the firm name in our logo usage. importantly, the names Quill and Marlow are separated by | not / and we use an ampersand not the word and.
On the front of the card, we want to include:
company logo and name (Quill|Marlow & Petrie)
on the back, we would definitely include:
address, email, cell #
logo and name (smaller size than front)

The variable will be location of individual name and title (mine for example is ) - whether on the front OR on the back. interested in variations from which to choose
Dr. Owen T. Caldecott, CFA
Scientifique des Fusées Financières

we would like to use contemporary symbols for address, email address, cell # with an option for web site that we do not intend to use initially. we like two sided cards and believe this design should use four rounded corners with the standard size. we prefer thicker card stock and may look at metal.

```html
<!DOCTYPE html>
<html lang="en">
<head>
<meta charset="utf-8">
<title>Quill|Marlow &amp; Petrie — Business Card</title>
<link rel="stylesheet" href="https://fonts.googleapis.com/css2?family=Lato:wght@400&family=Allura&display=swap">
<style>
  :root {
    --bg: #0a0a0a;
    --card: #151515;
    --card-edge: #1f1f1f;
    --grey: #7d7d7d;
    --grey-soft: #4a4a4a;
    --text: #9a9a9a;
    --orange: #e9821f;
  }
  * { box-sizing: border-box; margin: 0; padding: 0; }
  html, body {
    width: 1200px; height: 1004px; overflow: hidden;
    background: var(--bg);
    font-family: "Lato", Arial, sans-serif;
  }
  .sheet {
    width: 1200px; height: 1004px;
    display: flex; flex-direction: column;
    align-items: center; justify-content: center; gap: 40px;
  }
  .card {
    width: 770px; height: 440px;
    background: var(--card);
    border: 1px solid var(--card-edge);
    border-radius: 22px;
    position: relative;
  }
  /* Front */
  .card-front { display: flex; align-items: center; justify-content: center; gap: 34px; }
  .brand-mark { width: 96px; height: 96px; background: var(--grey-soft); }
  .brand-name { font-size: 50px; color: var(--grey); letter-spacing: 1px; }
  /* Back */
  .card-back { display: flex; align-items: center; padding: 0 60px; gap: 60px; }
  .brand-small { display: flex; align-items: center; gap: 16px; width: 300px; }
  .brand-small .brand-mark { width: 46px; height: 46px; background: var(--orange); }
  .brand-small .brand-name { font-size: 24px; }
  .contact { color: var(--text); font-size: 19px; line-height: 1.45; }
  .person-name { font-family: "Allura", cursive; color: var(--orange); font-size: 40px; line-height: 1.1; }
  .person-title { margin-bottom: 10px; }
  .contact-line { display: flex; align-items: center; gap: 10px; }
  .contact-line svg { width: 16px; height: 16px; flex: none; }
  .contact-line.address { padding-left: 26px; }
</style>
</head>
<body>
<main class="sheet">
  <section class="card card-front" aria-label="Card front">
    <span class="brand-mark" aria-hidden="true"></span>
    <span class="brand-name">Quill|Marlow &amp; Petrie</span>
  </section>

  <section class="card card-back" aria-label="Card back">
    <div class="brand-small">
      <span class="brand-mark" aria-hidden="true"></span>
      <span class="brand-name">Quill|Marlow &amp; Petrie</span>
    </div>
    <div class="contact">
      <p class="person-name">Dr. Owen T. Caldecott, CFA</p>
      <p class="person-title">Scientifique des Fusées Financières</p>
      <p class="contact-line address">41 Larch Lane 9th Floor</p>
      <p class="contact-line address">Harwick, NY 10214</p>
      <p class="contact-line">
        <svg viewBox="0 0 16 16" aria-hidden="true"><rect x="4" y="1" width="8" height="14" rx="1.5" fill="none" stroke="var(--orange)" stroke-width="1.6"/><line x1="7" y1="12.5" x2="9" y2="12.5" stroke="var(--orange)" stroke-width="1.4"/></svg>
        555-214-7730
      </p>
      <p class="contact-line">
        <svg viewBox="0 0 16 16" aria-hidden="true"><rect x="1" y="3" width="14" height="10" fill="var(--orange)"/><polyline points="1,3 8,9 15,3" fill="none" stroke="var(--card)" stroke-width="1.4"/></svg>
        hello@quillmarlow.example
      </p>
    </div>
  </section>
</main>
</body>
</html>
```